Maplerise Trading Inc. needs an innovative idea for letterhead and visiting cards.

Maplerise Trading Inc. is a Canadian brand since 2007. It is a renown dealer of kids and office furniture locally. Moreover, exporting electric fixtures e.g. switches, LED's, down-lights etc. to Middle East and Africa. We have initiated a number of steps including re-branding, to boost our export in 2020. We have successfully designed our new logo a few months ago through 'Artfolio' and now we are looking for an innovative idea for a letterhead.
Some key points:
• Red, black and white are the three colors used in all our packaging and furniture. (grey is optional)
• Shouldn’t be too wide.
• Use of watermark is preferable.
• You can visit our North American site at www.mapleriseinc.com. Export website of the company will be launched soon. www.mapleriseinc.ca
• Same letterhead will be used locally and internationally.
• Our new logo and sample packaging is attached.

```html
<!DOCTYPE html>
<html lang="en">
<head>
<meta charset="utf-8">
<title>Maplerise Trading Letterhead</title>
<link rel="stylesheet" href="https://fonts.googleapis.com/css2?family=Open+Sans:wght@400;600;700&display=swap">
<style>
  :root {
    --backdrop: #9e9e9e;
    --paper: #ffffff;
    --brand-red: #9c1b20;
    --brand-red-dark: #6d1015;
    --charcoal: #231f20;
    --mark-grey: #e6e4e4;
    --text: #2b2b2b;
  }
  * { margin: 0; padding: 0; box-sizing: border-box; }
  html, body { width: 1200px; height: 1200px; overflow: hidden; }
  body { background: var(--backdrop); position: relative; font-family: "Open Sans", sans-serif; }

  .letterhead {
    position: absolute; left: 204px; top: 45px;
    width: 793px; height: 1112px;
    background: var(--paper); overflow: hidden;
  }

  .header-band { position: absolute; left: 0; top: 0; width: 793px; height: 52px; }
  .tagline {
    position: absolute; left: 0; width: 793px; top: 26px;
    text-align: center; color: #fff;
    font-size: 14px; font-weight: 400; letter-spacing: 0.6px;
  }

  .brand { position: absolute; left: 0; width: 793px; top: 128px; display: flex; justify-content: center; align-items: center; gap: 12px; }
  .brand-dot { width: 22px; height: 22px; border-radius: 50%; background: var(--brand-red); }
  .brand-name { font-size: 24px; font-weight: 600; color: var(--brand-red); letter-spacing: 1px; line-height: 1; }

  .recipient { position: absolute; left: 102px; top: 289px; font-size: 12.5px; line-height: 18.75px; color: #111; }
  .salutation { position: absolute; left: 102px; top: 395px; font-size: 12.5px; color: #111; }

  .body-copy { position: absolute; left: 103px; top: 434px; font-size: 12.2px; color: var(--text); }
  .body-copy p { margin-bottom: 24px; }
  .body-copy span { display: block; white-space: nowrap; line-height: 25px; }

  .signature-mark {
    position: absolute; left: 101px; top: 829px; width: 106px; height: 30px;
    background: linear-gradient(90deg, rgba(43,43,43,0.18), rgba(43,43,43,0.06));
    border-radius: 14px;
  }
  .signer { position: absolute; left: 102px; top: 867px; line-height: 14px; }
  .signer-name { font-weight: 700; font-size: 12.5px; color: #111; }
  .signer-role { font-size: 12.5px; color: #333; }

  .watermark {
    position: absolute; left: 640px; top: 900px; width: 190px; height: 190px;
    border-radius: 50%; background: var(--mark-grey); opacity: 0.7;
  }

  .footer-band {
    position: absolute; left: 0; bottom: 0; width: 793px; height: 62px;
    background: var(--brand-red); color: #fff;
    display: flex; align-items: center; padding-left: 81px; gap: 22px;
    font-size: 9.4px;
  }
  .contact { display: flex; align-items: center; gap: 6px; white-space: nowrap; }
  .contact svg { width: 11px; height: 11px; fill: #fff; }
</style>
</head>
<body>
  <main class="letterhead">
    <svg class="header-band" viewBox="0 0 1269 83" preserveAspectRatio="none" aria-hidden="true">
      <rect x="0" y="0" width="1269" height="60" fill="var(--charcoal)"/>
      <polygon points="245,60 270,60 270,82" fill="var(--brand-red-dark)"/>
      <polygon points="1024,60 1000,60 1000,82" fill="var(--brand-red-dark)"/>
      <polygon points="292,23 977,23 1000,82 270,82" fill="var(--brand-red)"/>
    </svg>
    <div class="tagline">Built For Every Space</div>

    <div class="brand">
      <div class="brand-dot"></div>
      <div class="brand-name">MAPLERISE TRADING</div>
    </div>

    <div class="recipient">
      Mr/s<br>First &amp; Last name<br>Company Name<br>Address
    </div>
    <div class="salutation">Dear Sir</div>

    <section class="body-copy">
      <p>
        <span>This is a sample letter that has been placed to demonstrate typing remat (Your Company). letterhead</span>
        <span>design. When positioned properly, it will serve to work in harmony with all other elements letterhead.</span>
        <span>This letterhead design is meant to project an image</span>
      </p>
      <p>
        <span>This letterhead design is meant project an image of professionalism reliability. By using simple aligen</span>
        <span>we have created a very spacious feeling. The simplicity suggest&nbsp; rengththe spaciousnes contributes h</span>
        <span>aesthetics the layout. These basic qualities along with te (Your Company)</span>
      </p>
      <p>
        <span>look and helps reinforce the (Your Company) brand. letterhead design is meant to project an image p</span>
        <span>design. When positioned properly, it will serve to work in harmony all the other elements letterhead.</span>
        <span>sionalism and reliability.</span>
      </p>
      <p>
        <span>This letterhead design is based on the (Form of your logo) form (Your Company) logo. Each stationery</span>
        <span>we have created a very spacious feeling. The simplicity suggests strength the spaciousnes contribute</span>
        <span>part of the (Form of your logo).</span>
      </p>
    </section>

    <div class="signature-mark" role="img" aria-label="Handwritten signature of Dalen Harrow"></div>
    <div class="signer">
      <div class="signer-name">Dalen Harrow</div>
      <div class="signer-role">Manager</div>
    </div>

    <div class="watermark" aria-hidden="true"></div>

    <footer class="footer-band">
      <div class="contact">
        <svg viewBox="0 0 24 24"><path d="M12 1a8 8 0 0 0-8 8c0 6 8 14 8 14s8-8 8-14a8 8 0 0 0-8-8zm0 11a3 3 0 1 1 0-6 3 3 0 0 1 0 6z"/></svg>
        48 Alder Crescent, Unit 9, Oakvale
      </div>
      <div class="contact">
        <svg viewBox="0 0 24 24"><path d="M6.6 10.8a15 15 0 0 0 6.6 6.6l2.2-2.2a1 1 0 0 1 1-.25 11.4 11.4 0 0 0 3.6.57 1 1 0 0 1 1 1V20a1 1 0 0 1-1 1A17 17 0 0 1 3 4a1 1 0 0 1 1-1h3.5a1 1 0 0 1 1 1c0 1.25.2 2.45.57 3.57a1 1 0 0 1-.25 1z"/></svg>
        +1 (888) 555-0142
      </div>
      <div class="contact">
        <svg viewBox="0 0 24 24"><path d="M2 5h20v14H2z M2 5l10 8 10-8" fill="#fff" stroke="var(--brand-red)" stroke-width="1.6"/></svg>
        sales@mapleriseinc.com
      </div>
      <div class="contact">
        <svg viewBox="0 0 24 24"><circle cx="12" cy="12" r="9" fill="none" stroke="#fff" stroke-width="2"/><path d="M3 12h18M12 3c3 3 3 15 0 18M12 3c-3 3-3 15 0 18" fill="none" stroke="#fff" stroke-width="1.6"/></svg>
        www.mapleriseinc.com
      </div>
    </footer>
  </main>
</body>
</html>
```